8'x8' Exhibit Backdrop for Healthcare Events focused on the 55 and older crowds

8X8 Backdrop for Exhibiting.

I also want a design for a 6' table skirt to include our logo on two sides and the logo with Hereditary Cancer Screening underneath on the front. I want the main message of Will You Give your Loved Ones The Information To Beat Cancer in Their Lives to be completely centered on the 8X8 backdrop. Hereditary Cancer Screening The Test You Take For Them in the top left corner and the purple box on the right hand side - just like the photo that has been uploaded below. I need High resolution photos around the backdrop but not so large that they overtake the main message.

Target Market(s)

55+ crowd living in Adult only communities. They have an active lifestyle

Industry/Entity Type

Healthcare

Other font styles liked:
• "The Test You Take For Them" is Comic Sans

Colors
0255a3
fbed22
ffffff

Requirements
Must have
• I am posting a photo of the exact backdrop I would like to see. There are red arrows showing where to move certain items. There is a space underneath the slogan WILL YOU GIVE YOUR LOVED ONES... where another photo will go. Add another photo underneath the slogan that you are moving up - GIVE THEM THE GIFT OF KNOWLEDGE
• See the upload section for the new photo
• Do this one exactly like I am asking for and then you can show me some of your ideas. Thanks
• THE PHOTOS UPLOADED ARE EXAMPLES. FEEL FREE TO SEARCH OUT YOUR OWN HIGH RESOLUTION PHOTOS. THANKS

```html
<!DOCTYPE html>
<html lang="en">
<head>
<meta charset="utf-8">
<title>Hereditary Cancer Screening Backdrop</title>
<link rel="stylesheet" href="https://fonts.googleapis.com/css2?family=Arimo:wght@400;700&family=Roboto+Condensed:wght@400;700&family=Comic+Neue:wght@700&family=Delius&family=Open+Sans:wght@600;700&display=swap">
<style>
  :root {
    --navy: #1b2079;
    --panel-navy: #17196b;
    --title-navy: #1d2a86;
    --green: #5cf01c;
    --ink: #0d0d0d;
    --white: #ffffff;
    --photo-warm-a: #d9b89a;
    --photo-warm-b: #8f6e57;
    --photo-green-a: #9cbf6e;
    --photo-violet-a: #6e6fc4;
    --photo-violet-b: #27287a;
    --photo-grey-a: #d6d6d6;
    --photo-grey-b: #6b6b6b;
  }
  * { box-sizing: border-box; margin: 0; padding: 0; }
  html, body { width: 1200px; height: 1200px; overflow: hidden; background: var(--white); }
  .backdrop { position: relative; width: 1200px; height: 1200px; background: var(--white); }

  .photo { position: absolute; }
  .photo--family-outdoor { left: 378px; top: 18px; width: 362px; height: 285px; background: linear-gradient(160deg, var(--photo-green-a), var(--photo-warm-a) 55%, #f1d6c9); }
  .photo--grandfather-girl { left: 4px; top: 320px; width: 238px; height: 245px; background: linear-gradient(135deg, #e8e4da, #c98a7a 55%, var(--photo-warm-b)); }
  .photo--grandparents-kids { left: 4px; top: 570px; width: 240px; height: 235px; background: linear-gradient(135deg, #e2d5c4, var(--photo-warm-a) 50%, #6f86b8); }
  .photo--family-baby { left: 292px; top: 760px; width: 450px; height: 390px; background: linear-gradient(150deg, #eadbcc, var(--photo-warm-a) 50%, #c99aa0); }
  .photo--bridge { left: 0; top: 0; width: 100%; height: 370px; background: linear-gradient(180deg, var(--photo-violet-a), #5a5bb6 55%, var(--panel-navy)); }
  .photo--grid-a { left: 762px; top: 800px; width: 212px; height: 165px; background: linear-gradient(135deg, #b98e74, #5b3a2c); }
  .photo--grid-b { left: 982px; top: 808px; width: 218px; height: 160px; background: linear-gradient(135deg, var(--photo-grey-a), var(--photo-grey-b)); }
  .photo--grid-c { left: 762px; top: 972px; width: 210px; height: 168px; background: linear-gradient(135deg, var(--photo-grey-b), var(--photo-grey-a)); }
  .photo--grid-d { left: 982px; top: 975px; width: 218px; height: 170px; background: linear-gradient(135deg, #e5d7c8, var(--photo-warm-a) 50%, #5f7fc0); }

  .title-block { position: absolute; left: 20px; top: 70px; width: 330px; text-align: right; font-family: "Arimo", sans-serif; color: var(--title-navy); line-height: 1.02; }
  .title-block__strong { display: block; font-size: 58px; font-weight: 700; letter-spacing: -0.5px; }
  .title-block__line { display: block; font-size: 62px; font-weight: 400; }
  .title-block__tagline { display: block; margin-top: 12px; margin-left: 6px; background: var(--green); color: var(--white); font-family: "Comic Neue", cursive; font-weight: 700; font-size: 18px; line-height: 26px; text-align: center; }

  .main-message { position: absolute; left: 248px; top: 332px; width: 508px; font-family: "Roboto Condensed", sans-serif; color: var(--ink); line-height: 1; }
  .main-message__line { display: block; font-size: 64px; font-weight: 400; letter-spacing: -1px; padding-left: 22px; }
  .main-message__line strong { font-weight: 700; }
  .main-message__bar { display: block; margin-top: 6px; background: var(--ink); color: var(--white); font-size: 38px; padding: 2px 0 0 22px; height: 46px; }
  .main-message__cancer { display: block; color: var(--green); font-size: 150px; font-weight: 400; letter-spacing: -4px; padding-left: 20px; margin-top: 0; line-height: 0.95; }
  .main-message__close { display: block; font-size: 66px; padding-left: 22px; letter-spacing: -1px; }

  .frame-rule--top { position: absolute; left: 248px; top: 712px; width: 510px; height: 14px; background: var(--ink); }
  .frame-rule--side { position: absolute; left: 268px; top: 712px; width: 12px; height: 440px; background: var(--ink); }

  .knowledge-panel { position: absolute; left: 756px; top: 0; width: 444px; height: 782px; background: var(--panel-navy); overflow: hidden; }
  .knowledge-panel__heading { position: absolute; right: 44px; top: 410px; text-align: right; color: var(--white); font-family: "Arimo", sans-serif; line-height: 1; }
  .knowledge-panel__give { font-size: 40px; }
  .knowledge-panel__give strong { font-weight: 700; }
  .knowledge-panel__gift { display: block; font-family: "Roboto Condensed", sans-serif; font-size: 28px; }
  .knowledge-panel__knowledge { display: block; font-size: 38px; font-weight: 700; letter-spacing: 0.5px; }
  .knowledge-panel__note { position: absolute; right: 44px; top: 560px; width: 320px; text-align: right; color: var(--white); font-family: "Delius", cursive; font-size: 23px; line-height: 1.45; }
  .knowledge-panel__icon { position: absolute; right: 48px; top: 640px; width: 86px; height: 90px; }
  .knowledge-panel__power { position: absolute; right: 44px; top: 742px; color: var(--green); font-family: "Arimo", sans-serif; font-weight: 700; font-size: 20px; display: flex; align-items: center; gap: 2px; }
  .knowledge-panel__power::before { content: ""; width: 14px; height: 14px; background: var(--green); }

  .brand { position: absolute; left: 40px; top: 955px; display: flex; align-items: center; gap: 12px; }
  .brand__mark { width: 40px; height: 40px; border-radius: 50%; background: var(--navy); }
  .brand__name { font-family: "Arimo", sans-serif; font-weight: 700; font-size: 24px; line-height: 1.05; color: var(--navy); letter-spacing: 1px; }

  .web-address { position: absolute; left: 770px; top: 1160px; width: 420px; text-align: center; font-family: "Open Sans", sans-serif; font-weight: 700; font-size: 21px; color: var(--ink); }
</style>
</head>
<body>
<main class="backdrop">

  <header class="title-block">
    <span class="title-block__strong">Hereditary</span>
    <span class="title-block__line">Cancer</span>
    <span class="title-block__line">Screening</span>
    <span class="title-block__tagline">"The Test You Take For Them"</span>
  </header>

  <div class="photo photo--family-outdoor" role="img" aria-label="Photo of a smiling three-generation family outdoors"></div>
  <div class="photo photo--grandfather-girl" role="img" aria-label="Photo of a grandfather with glasses and his granddaughter laughing"></div>
  <div class="photo photo--grandparents-kids" role="img" aria-label="Photo of grandparents hugging two grandchildren"></div>

  <section class="main-message">
    <span class="main-message__line">WILL YOU <strong>GIVE</strong></span>
    <span class="main-message__line">YOUR LOVED ONES</span>
    <span class="main-message__bar">THE INFORMATION TO BEAT</span>
    <span class="main-message__cancer">CANCER</span>
    <span class="main-message__close">IN THEIR LIVES ?</span>
  </section>

  <div class="frame-rule--top"></div>
  <div class="frame-rule--side"></div>

  <div class="photo photo--family-baby" role="img" aria-label="Photo of grandparents, parents and children gathered around a newborn baby"></div>

  <aside class="knowledge-panel">
    <div class="photo photo--bridge" role="img" aria-label="Violet-toned photo of a grandmother and grandchildren sitting on a wooden bridge in the woods"></div>
    <h2 class="knowledge-panel__heading">
      <span class="knowledge-panel__give"><strong>GIVE</strong> THEM</span>
      <span class="knowledge-panel__gift">THE GIFT OF</span>
      <span class="knowledge-panel__knowledge">KNOWLEDGE</span>
    </h2>
    <p class="knowledge-panel__note">Knowing is better than not knowing.</p>
    <svg class="knowledge-panel__icon" viewBox="0 0 86 90" aria-hidden="true">
      <g fill="none" stroke="#5cf01c" stroke-width="7" stroke-linecap="round">
        <path d="M33 72 C30 60 20 56 20 44 C20 32 30 26 40 26 C52 26 62 34 60 48 C59 56 52 62 52 72 Z"/>
        <line x1="36" y1="82" x2="52" y2="82"/>
        <line x1="40" y1="6" x2="40" y2="14"/>
        <line x1="14" y1="14" x2="20" y2="20"/>
        <line x1="66" y1="14" x2="60" y2="20"/>
        <line x1="4" y1="40" x2="10" y2="40"/>
        <line x1="76" y1="40" x2="82" y2="40"/>
      </g>
    </svg>
    <p class="knowledge-panel__power">Knowledge is Power</p>
  </aside>

  <div class="photo photo--grid-a" role="img" aria-label="Photo of a grandfather and granddaughter cheek to cheek"></div>
  <div class="photo photo--grid-b" role="img" aria-label="Black and white photo of a grandmother hugged by her granddaughter"></div>
  <div class="photo photo--grid-c" role="img" aria-label="Black and white photo of a girl hugging her grandmother"></div>
  <div class="photo photo--grid-d" role="img" aria-label="Photo of grandparents smiling with their grandchildren"></div>

  <div class="brand">
    <span class="brand__mark"></span>
    <span class="brand__name">CLEARPATH<br>HEALTH<br>GROUP</span>
  </div>

  <p class="web-address">www.kinshipscreening.com</p>

</main>
</body>
</html>
```